Healthcare website - Diabetic Shoes - Elderfund - No Cost

I am looking to upgrade my website. I do not want to use Wordpress, Adobe Muse or another designing program. The code should be easily editable using textpad or VI. After the project is done I want to easily add my custom PHP code.

Features
Creative and Modern Design .
Fully responsive site for use on mobile devices
bootstrap, jquery

My current website is
www.pebblewalkco.com

Target Market(s)

Older people who have diabetes. Target market is +60 years old, but we do have younger people going to the site to help out their parents.

Industry/Entity Type

Healthcare

Coding

Coded - Design and coding required

Number of Pages Required

2 page

Colors

Designer to choose colors to be used in the design.

Requirements
Must have
• The code should be easily editable using textpad or VI. After the project is done I want to easily add my custom PHP code.
• The first page will be the home page and the other page I need is this form.
• https://www.pebblewalkco.com/pebble-walk-co-do-i-qualify.php
Should not have
• I do not want to use Wordpress, Adobe Muse or another designing program.

```html
<!DOCTYPE html>
<html lang="en">
<head>
<meta charset="utf-8">
<title>Pebble Walk Co – Diabetic Shoes Covered by Elderfund</title>
<link rel="stylesheet" href="https://fonts.googleapis.com/css2?family=Roboto:wght@400;500;700&family=Open+Sans:wght@400;600&display=swap">
<style>
:root{
  --green:#6cc04a;
  --brand:#2f8a8c;
  --blue:#2b6ea3;
  --heading:#2f6b9a;
  --form-bg:#4b7aa0;
  --sky:#29a8e0;
  --text:#6b6b6b;
  --footer:#2b74b8;
  --footer-dark:#111;
  --orange:#f5a12a;
  --white:#fff;
}
*{box-sizing:border-box;margin:0;padding:0}
html,body{width:1200px;height:3346px;overflow:hidden}
body{position:relative;background:var(--white);font-family:"Open Sans",Arial,sans-serif;color:var(--text)}
.abs{position:absolute}

/* header */
.site-header{left:0;top:0;width:1200px;height:67px}
.brand{left:130px;top:10px;font-family:"Roboto",sans-serif;font-weight:500;font-size:36px;color:var(--brand);letter-spacing:.5px}
.contact{right:130px;top:16px;display:flex;align-items:center;gap:8px;font-family:"Roboto",sans-serif;font-weight:700;font-size:26px;color:var(--blue)}
.social-mini{display:flex;gap:4px;margin-left:8px}
.social-mini span{width:22px;height:22px;background:var(--blue);border-radius:3px}

/* nav */
.main-nav{left:0;top:67px;width:1200px;height:49px;background:var(--green);display:flex;align-items:center;padding-left:132px;font-family:"Roboto",sans-serif;font-weight:700;font-size:13px;color:var(--white)}
.main-nav a{color:var(--white);text-decoration:none;padding:0 14px;height:49px;line-height:49px;display:block}
.main-nav a.active{background:var(--blue)}
.main-nav .login{background:var(--blue);border-radius:14px;height:28px;line-height:28px;padding:0 26px;margin-left:14px}

/* hero */
.hero{left:0;top:116px;width:1200px;height:491px;background:linear-gradient(135deg,#6b8a4a 0%,#4a4a38 45%,#8a6a48 75%,#5a4432 100%)}
.hero-copy{left:629px;top:186px;width:430px;color:var(--white)}
.hero-title{font-family:"Roboto",sans-serif;font-weight:700;font-size:52px;line-height:1}
.hero-title span{color:var(--green)}
.hero-sub{font-family:"Roboto",sans-serif;font-weight:700;font-size:21px;margin-top:2px}
.hero-note{font-size:12.5px;line-height:1.45;margin-top:12px}

/* steps */
.steps-title{left:0;top:642px;width:1200px;text-align:center;font-family:"Roboto",sans-serif;font-size:25px;color:var(--heading)}
.step{top:714px;width:240px;text-align:center;font-size:15px;line-height:1.3;color:#333}
.step-icon{width:112px;height:112px;border-radius:50%;background:var(--sky);margin:0 auto 14px;display:flex;align-items:center;justify-content:center}

/* form */
.catalog{left:0;top:937px;width:1200px;height:696px;background:var(--form-bg)}
.catalog-title{left:0;top:983px;width:1200px;text-align:center;font-family:"Roboto",sans-serif;font-weight:700;font-size:35px;color:var(--white)}
.field{height:54px;background:var(--white);border-radius:3px;font-size:13px;color:#666;padding:0 14px;display:flex;align-items:center;justify-content:space-between}
.field.left{left:167px;width:431px}
.field.right{left:616px;width:417px}
.caret{width:0;height:0;border-left:7px solid transparent;border-right:7px solid transparent;border-top:8px solid var(--sky)}
.field.tall{height:58px;align-items:center}
.submit{left:346px;top:1508px;width:508px;height:74px;background:var(--green);border-radius:3px;color:var(--white);font-family:"Roboto",sans-serif;font-weight:700;font-size:24px;display:flex;align-items:center;justify-content:center}

/* content */
.info-title{font-family:"Roboto",sans-serif;font-weight:700;font-size:38px;line-height:1.22;color:var(--heading)}
.info-text{font-size:14.5px;line-height:1.6;color:var(--text)}
.photo{border-radius:0}

/* products */
.products-title{left:0;top:2808px;width:1200px;text-align:center;font-family:"Roboto",sans-serif;font-size:38px;color:#555}
.product{top:2879px;width:196px;height:274px;background:#f1f1f1;display:flex;align-items:center;justify-content:center}
.product-shape{width:90px;height:150px;background:linear-gradient(#555,#222);border-radius:10px}

/* footer */
.site-footer{left:0;top:3185px;width:1200px;height:122px;background:var(--footer);color:var(--white);font-family:"Roboto",sans-serif}
.f-label{font-weight:700;font-size:15px}
.f-social span{display:inline-block;width:36px;height:36px;border:2px solid var(--white);border-radius:3px;margin-right:8px}
.newsletter{display:flex}
.newsletter .input{width:220px;height:36px;background:var(--white);color:#777;font-size:13px;padding:0 10px;line-height:36px;font-family:"Open Sans",sans-serif}
.newsletter .btn{width:82px;height:36px;background:var(--orange);font-weight:700;font-size:13px;text-align:center;line-height:36px}
.badge{background:var(--white);border-radius:2px}
.news-text{font-size:16px;line-height:1.35}
.footer-bar{left:0;top:3307px;width:1200px;height:39px;background:var(--footer-dark);color:var(--white);font-family:"Roboto",sans-serif;font-size:11px;font-weight:700;display:flex;align-items:center;justify-content:space-between;padding:0 130px}
</style>
</head>
<body>

<header class="site-header abs">
  <div class="brand abs">Pebble Walk Co</div>
  <div class="contact abs">
    <svg width="24" height="24" viewBox="0 0 24 24"><circle cx="12" cy="12" r="12" fill="#6cc04a"/><path d="M8 6c1 0 2 2.5 2 3s-1 1-1 1.5 2.5 4 4 4.5c.5 0 1-1 1.5-1s3 1 3 2-1.5 2.5-2.5 2.5C10 18.5 5.5 14 5.5 9 5.5 8 7 6 8 6z" fill="#fff"/></svg>
    1-800-555-0147
    <div class="social-mini"><span></span><span></span></div>
  </div>
</header>

<nav class="main-nav abs">
  <a class="active">HOME</a>
  <a>PEBBLE WALK CO! DO I QUALIFY!</a>
  <a>WHY DIABETIC SHOES?</a>
  <a>SHOES</a>
  <a>PRODUCTS</a>
  <a>SHOE FITTER JOBS</a>
  <a>FAQ</a>
  <a class="login">LOGIN</a>
</nav>

<section class="hero abs" role="img" aria-label="Close-up of a walker's running shoe stepping on an autumn path"></section>
<div class="hero-copy abs">
  <div class="hero-title">DIABETIC <span>SHOES</span></div>
  <div class="hero-sub">OR SNEAKERS COVERED BY ELDERFUND</div>
  <p class="hero-note">No or little out of pocket Cost To You!* Elderfund, and most insurance plans, may cover the cost of one pair of diabetic shoes and three pairs of custom inserts per calendar year. Co-payments, deductibles and some restrictions apply.</p>
</div>

<h2 class="steps-title abs">4 Easy Steps To Receive Your New Therapeutic Shoes.</h2>
<div class="step abs" style="left:92px">
  <div class="step-icon"><svg width="46" height="56" viewBox="0 0 46 56"><path d="M3 3h28l12 12v38H3z" fill="none" stroke="#fff" stroke-width="3"/><path d="M11 22h24M11 30h24M11 38h24M11 46h16" stroke="#fff" stroke-width="3"/></svg></div>
  Fill out an application<br>to see if you qualify.
</div>
<div class="step abs" style="left:355px">
  <div class="step-icon"><svg width="50" height="58" viewBox="0 0 50 58"><rect x="3" y="7" width="36" height="48" fill="none" stroke="#fff" stroke-width="3"/><rect x="13" y="2" width="16" height="9" fill="#fff"/><path d="M10 22h22M10 30h22M10 38h22M10 46h14" stroke="#fff" stroke-width="3"/><path d="M44 14v34l2 6 2-6V14z" fill="#fff"/></svg></div>
  A prescription will be<br>faxed to your primary<br>physician.
</div>
<div class="step abs" style="left:616px">
  <div class="step-icon"><svg width="60" height="36" viewBox="0 0 60 36"><path d="M4 12c6 0 12-4 16-10 6 6 14 10 24 12 8 2 12 6 12 12v4H4z" fill="#fff"/><path d="M4 34h52" stroke="#fff" stroke-width="3"/></svg></div>
  After the prescription is<br>signed, a certified shoe fitter<br>will fit your new shoes.
</div>
<div class="step abs" style="left:879px">
  <div class="step-icon"><svg width="60" height="50" viewBox="0 0 60 50"><rect x="6" y="12" width="12" height="22" fill="#fff"/><rect x="42" y="12" width="12" height="22" fill="#fff"/><path d="M18 20h24" stroke="#fff" stroke-width="4"/><rect x="26" y="22" width="8" height="10" fill="#fff"/><path d="M8 34v14M16 34v14M44 34v14M52 34v14" stroke="#fff" stroke-width="3"/></svg></div>
  Enjoy your new shoes!
</div>

<section class="catalog abs"></section>
<h2 class="catalog-title abs">REQUEST A FREE DIABETIC SHOE CATALOG</h2>
<div class="field left abs" style="top:1071px">First Name</div>
<div class="field right abs" style="top:1071px">Last Name</div>
<div class="field left abs" style="top:1138px">Address</div>
<div class="field right abs" style="top:1138px">City</div>
<div class="field left abs" style="top:1207px">State</div>
<div class="field right abs" style="top:1207px">Zip</div>
<div class="field left abs" style="top:1274px">Phone</div>
<div class="field right abs" style="top:1274px">Best time to Call</div>
<div class="field left abs" style="top:1343px">Email</div>
<div class="field right abs" style="top:1343px">Primary Insurance <span class="caret"></span></div>
<div class="field left tall abs" style="top:1412px">Do you want to check eligibility Online? <span class="caret"></span></div>
<div class="field right tall abs" style="top:1412px">Comments</div>
<div class="submit abs">Request Catalog</div>

<h3 class="info-title abs" style="left:127px;top:1726px;width:460px">How Does Diabetes Cause Foot Problems?</h3>
<p class="info-text abs" style="left:127px;top:1838px;width:440px">Diabetes can cause neuropathy (nerve damage), which reduces feeling in your feet. This makes you less likely to feel the early warning signs of foot problems. Decreased circulation reduces the ability to heal and fight off infection. These two conditions significantly increase the likelihood of foot complications, infection, and ulceration.</p>
<div class="photo abs" style="left:609px;top:1713px;width:459px;height:285px;background:linear-gradient(160deg,#a85a48,#6a3a30 60%,#3a2a28)" role="img" aria-label="Feet in brown leather comfort shoes on a wooden deck"></div>

<div class="photo abs" style="left:127px;top:2036px;width:460px;height:290px;background:linear-gradient(135deg,#f2f2f2,#9a9a9a 50%,#8a4a2a)" role="img" aria-label="Assortment of therapeutic sneakers and leather shoes"></div>
<h3 class="info-title abs" style="left:609px;top:2046px;width:470px">Why Are Properly Fitted Shoes Important?</h3>
<p class="info-text abs" style="left:609px;top:2160px;width:455px">Twenty four million people have diabetes, and twenty-five percent of this population will develop foot problems caused by their disease. We provide the most fashionable orthopedic shoes available, in a variety of styles and brands, to help treat and prevent painful diabetic symptoms.</p>
<p class="info-text abs" style="left:609px;top:2298px;width:455px">Our orthopedic shoes reduce the pressure and friction on your feet that can lead to foot injuries.</p>
<p class="info-text abs" style="left:127px;top:2348px;width:946px">Custom inserts relieve pressure and cushion your feet. Diabetic Socks and our therapeutic shoes are also accurately sized and padded to ensure that there is enough room in the toe-box, heel, and arch of the shoe. All of these features provide you with the very best in comfort and help prevent potential foot complications.</p>

<h3 class="info-title abs" style="left:127px;top:2466px;width:440px">How Do You Know If Orthopedic Shoes Are Right For You?</h3>
<p class="info-text abs" style="left:127px;top:2622px;width:450px">Anyone with Diabetic Neuropathy, poor circulation, high risk of infection or nerve damage can benefit from diabetic socks and our shoes. Elderfund patients who qualify are eligible for one pair of shoes and three sets of custom insoles per year - at no out of pocket cost to them. Additionally, most private insurance companies will cover the same benefits as Elderfund.</p>
<div class="photo abs" style="left:609px;top:2455px;width:459px;height:286px;background:linear-gradient(160deg,#3a2030,#7a2a5a 55%,#2a1a24)" role="img" aria-label="Feet in grey and orange athletic shoes on a wooden floor"></div>

<h2 class="products-title abs">CLICK HERE FOR OUR ELDERFUND PRODUCTS</h2>
<div class="product abs" style="left:127px" role="img" aria-label="Handheld electrotherapy unit with electrode pads"><div class="product-shape" style="width:44px;height:140px"></div></div>
<div class="product abs" style="left:379px" role="img" aria-label="Black lift seat cushion"><div class="product-shape" style="width:110px;height:100px;border-radius:50% 50% 10px 10px"></div></div>
<div class="product abs" style="left:631px" role="img" aria-label="Compression therapy wrap"><div class="product-shape" style="width:80px;height:110px;background:linear-gradient(#9ab,#345)"></div></div>
<div class="product abs" style="left:877px" role="img" aria-label="Black wrist and ankle braces"><div class="product-shape" style="width:70px;height:170px"></div></div>

<footer class="site-footer abs">
  <div class="f-label abs" style="left:130px;top:28px">FOLLOW US</div>
  <div class="f-social abs" style="left:130px;top:56px"><span></span><span></span></div>
  <div class="f-label abs" style="left:262px;top:28px">SING UP FOR NEWSLETTER</div>
  <div class="newsletter abs" style="left:262px;top:56px"><div class="input">Email..</div><div class="btn">SIGN UP</div></div>
  <div class="badge abs" style="left:617px;top:32px;width:44px;height:58px"></div>
  <div class="badge abs" style="left:671px;top:58px;width:58px;height:32px"></div>
  <div class="f-label abs" style="left:770px;top:30px">LATEST NEWS</div>
  <p class="news-text abs" style="left:770px;top:54px;width:320px">Lorem ipsum dolor sit amet, cmassa. Cum sociis natoque tibus</p>
</footer>
<div class="footer-bar abs">
  <span>TERMS OF USE &nbsp;|&nbsp; PRIVACY POLICY &nbsp;|&nbsp; RETURN/EXCHANGE</span>
  <span>© 2017 Pebble Walk Co - All Rights Reserved</span>
</div>

</body>
</html>
```